Roofing Company Sales Rep Business Card

Business card for sales rep to canvass and hand out to property owners/managers for free roof inspections and roof replacements.

```html
<!DOCTYPE html>
<html lang="en">
<head>
<meta charset="utf-8">
<title>Ridgeline Roofing – Business Card</title>
<link href="https://fonts.googleapis.com/css2?family=Roboto:wght@400;700;900&display=swap" rel="stylesheet">
<style>
  :root {
    --brand-red: #e3100f;
    --ink: #0a0a0a;
    --paper: #f4f1f0;
    --white: #ffffff;
    --backdrop: #e6e3e1;
  }
  html, body {
    margin: 0;
    padding: 0;
    width: 1200px;
    height: 900px;
    overflow: hidden;
    background: var(--backdrop);
    font-family: "Roboto", Arial, sans-serif;
  }
  .business-card {
    position: absolute;
    left: 100px;
    top: 140px;
    width: 1000px;
    height: 620px;
    box-shadow: 0 18px 40px rgba(0,0,0,0.18);
    overflow: hidden;
  }
  .card-header {
    position: absolute;
    left: 0; top: 0;
    width: 100%;
    height: 320px;
    background: radial-gradient(ellipse at 50% 55%, var(--white) 0%, var(--paper) 70%, #e9e4e3 100%);
  }
  .wordmark {
    position: absolute;
    left: 0; right: 0;
    top: 118px;
    display: flex;
    align-items: center;
    justify-content: center;
    gap: 22px;
  }
  .wordmark-square {
    width: 34px;
    height: 34px;
    background: var(--brand-red);
  }
  .wordmark-name {
    font-weight: 900;
    font-size: 74px;
    letter-spacing: 3px;
    color: var(--ink);
    text-transform: uppercase;
    line-height: 1;
  }
  .accent-rule {
    position: absolute;
    left: 0; top: 320px;
    width: 100%;
    height: 9px;
    background: var(--brand-red);
  }
  .card-body {
    position: absolute;
    left: 0; top: 329px;
    width: 100%;
    height: 291px;
    background: var(--ink);
    color: var(--white);
  }
  .rep-identity {
    position: absolute;
    right: 545px;
    top: 52px;
    text-align: right;
  }
  .rep-name {
    font-weight: 900;
    font-size: 41px;
    color: var(--brand-red);
    text-transform: uppercase;
    line-height: 1.05;
    margin: 0;
  }
  .rep-title {
    font-size: 28px;
    margin: 2px 0 0;
    line-height: 1.2;
  }
  .divider {
    position: absolute;
    left: 493px;
    top: 48px;
    width: 2px;
    height: 96px;
    background: var(--white);
  }
  .contact-list {
    position: absolute;
    left: 521px;
    top: 42px;
    margin: 0;
    padding: 0;
    list-style: none;
    font-size: 27px;
    line-height: 36px;
  }
  .contact-list li {
    display: flex;
    align-items: center;
    gap: 8px;
  }
  .contact-icon {
    width: 26px;
    height: 26px;
    flex: none;
  }
  .address {
    position: absolute;
    left: 0; right: 0;
    top: 162px;
    text-align: center;
    font-size: 27px;
    margin: 0;
  }
  .offer-banner {
    position: absolute;
    left: 138px;
    top: 224px;
    width: 711px;
    height: 64px;
    background: var(--white);
    display: flex;
    align-items: center;
    justify-content: center;
    font-weight: 700;
    font-size: 28px;
    color: var(--brand-red);
  }
</style>
</head>
<body>
  <article class="business-card">
    <header class="card-header">
      <div class="wordmark">
        <span class="wordmark-square"></span>
        <span class="wordmark-name">Ridgeline Roofing</span>
      </div>
    </header>
    <div class="accent-rule"></div>
    <section class="card-body">
      <div class="rep-identity">
        <p class="rep-name">Marcus Delaney</p>
        <p class="rep-title">Managing Director</p>
      </div>
      <div class="divider"></div>
      <ul class="contact-list">
        <li>
          <svg class="contact-icon" viewBox="0 0 24 24" aria-hidden="true">
            <path fill="var(--brand-red)" d="M6.6 10.8a15.1 15.1 0 0 0 6.6 6.6l2.2-2.2a1 1 0 0 1 1-.25 11.4 11.4 0 0 0 3.6.57 1 1 0 0 1 1 1V20a1 1 0 0 1-1 1A17 17 0 0 1 3 4a1 1 0 0 1 1-1h3.5a1 1 0 0 1 1 1c0 1.25.2 2.45.57 3.57a1 1 0 0 1-.25 1z"/>
          </svg>
          044-555 218 640
        </li>
        <li>
          <svg class="contact-icon" viewBox="0 0 24 24" aria-hidden="true">
            <rect x="2" y="5" width="20" height="14" fill="var(--brand-red)"/>
            <path d="M2 5l10 8 10-8" fill="none" stroke="var(--ink)" stroke-width="1.6"/>
          </svg>
          hello@ridgelineroof.com
        </li>
        <li>
          <svg class="contact-icon" viewBox="0 0 24 24" aria-hidden="true">
            <g fill="none" stroke="var(--brand-red)" stroke-width="1.8">
              <circle cx="12" cy="12" r="9.5"/>
              <ellipse cx="12" cy="12" rx="4.2" ry="9.5"/>
              <path d="M2.5 12h19M4 7h16M4 17h16"/>
            </g>
          </svg>
          www.ridgelineroof.com
        </li>
      </ul>
      <p class="address">88 Harbor Lane, Suite 4, 70318 Westland</p>
      <div class="offer-banner">FREE Roof Inspections and Roof Replacements</div>
    </section>
  </article>
</body>
</html>
```